Vornel Technologies business card design

We need a business card designed with our new logo. it would be great if the card could communicate it is a technology based company.

Target Market(s)

system integrators

Industry/Entity Type

technology, IOT

Contact Information for Business Card

Name, designation, Address, telephone number, email address

Requirements
Must have
• logo and company name
Nice to have
• something to do with technology

```html
<!DOCTYPE html>
<html lang="en">
<head>
<meta charset="utf-8">
<title>Vornel Technologies — Business Card</title>
<link rel="stylesheet" href="https://fonts.googleapis.com/css2?family=Arimo:wght@400;700&display=swap">
<style>
  :root {
    --orange-deep: #d2451c;
    --orange-warm: #e25a18;
    --orange-bright: #f07c12;
    --accent: #f39322;
    --ink: #1e1e1e;
    --logo-ink: #3a3a3a;
    --paper: #ffffff;
  }
  * { margin: 0; padding: 0; box-sizing: border-box; }
  html, body {
    width: 1200px;
    height: 785px;
    overflow: hidden;
    background: var(--paper);
  }
  .card {
    position: relative;
    width: 1200px;
    height: 785px;
    background: var(--paper);
    font-family: "Arimo", Arial, sans-serif;
    color: var(--ink);
  }
  .brand-panel {
    position: absolute;
    left: 0; top: 0;
    width: 458px;
    height: 785px;
    background: linear-gradient(215deg, var(--orange-deep) 0%, var(--orange-warm) 55%, var(--orange-bright) 100%);
  }
  .brand-panel__mark {
    position: absolute;
    left: 62px;
    top: 324px;
    width: 72px;
    height: 72px;
    border-radius: 50%;
    background: var(--paper);
  }
  .brand-panel__name {
    position: absolute;
    left: 160px;
    top: 328px;
    color: var(--paper);
    font-weight: 700;
    line-height: 1;
  }
  .brand-panel__name .word {
    display: block;
    font-size: 50px;
    letter-spacing: 1px;
  }
  .brand-panel__name .tagline {
    display: block;
    font-size: 14px;
    letter-spacing: 7.4px;
    margin-top: 6px;
  }
  .wordmark {
    position: absolute;
    left: 664px;
    top: 66px;
    color: var(--logo-ink);
    font-weight: 700;
    line-height: 1;
  }
  .wordmark .word {
    display: block;
    font-size: 84px;
    letter-spacing: 2px;
  }
  .wordmark .tagline {
    display: block;
    font-size: 24px;
    letter-spacing: 12.6px;
    margin-top: 10px;
  }
  .contact-list {
    position: absolute;
    left: 548px;
    top: 0;
    list-style: none;
  }
  .contact-item {
    position: absolute;
    left: 0;
    display: flex;
    align-items: flex-start;
    white-space: nowrap;
  }
  .contact-item--phone { top: 242px; }
  .contact-item--email { top: 351px; }
  .contact-item--web { top: 459px; }
  .contact-item--address { top: 568px; }
  .contact-icon {
    width: 68px;
    height: 68px;
    flex: none;
  }
  .contact-text {
    margin-left: 50px;
    font-size: 36px;
    line-height: 68px;
    font-weight: 400;
  }
  .contact-item--phone .contact-text { margin-left: 42px; }
  .contact-text--address {
    line-height: 55px;
    margin-top: 6px;
  }
</style>
</head>
<body>
  <main class="card">
    <section class="brand-panel">
      <span class="brand-panel__mark"></span>
      <div class="brand-panel__name">
        <span class="word">VORNEL</span>
        <span class="tagline">TECHNOLOGIES</span>
      </div>
    </section>

    <div class="wordmark">
      <span class="word">VORNEL</span>
      <span class="tagline">TECHNOLOGIES</span>
    </div>

    <ul class="contact-list">
      <li class="contact-item contact-item--phone">
        <svg class="contact-icon" viewBox="0 0 68 68" aria-hidden="true">
          <circle cx="34" cy="34" r="34" fill="var(--accent)"/>
          <path d="M24 19c2-1 4 0 5 2l3 6c1 2 0 3-1 4l-2 2c1 4 5 8 9 10l2-2c1-1 3-2 4-1l6 3c2 1 3 3 2 5l-2 3c-2 2-5 3-8 2-10-3-18-11-21-21-1-3 0-6 2-8z" fill="none" stroke="#fff" stroke-width="3" stroke-linejoin="round"/>
        </svg>
        <span class="contact-text">+44 (0)117 496 0123</span>
      </li>
      <li class="contact-item contact-item--email">
        <svg class="contact-icon" viewBox="0 0 68 68" aria-hidden="true">
          <circle cx="34" cy="34" r="34" fill="var(--accent)"/>
          <rect x="19" y="23" width="30" height="22" rx="2" fill="none" stroke="#fff" stroke-width="3"/>
          <path d="M20 25l14 11 14-11" fill="none" stroke="#fff" stroke-width="3" stroke-linejoin="round"/>
        </svg>
        <span class="contact-text">sales@vorneltech.com</span>
      </li>
      <li class="contact-item contact-item--web">
        <svg class="contact-icon" viewBox="0 0 68 68" aria-hidden="true">
          <circle cx="34" cy="34" r="34" fill="var(--accent)"/>
          <g fill="none" stroke="#fff" stroke-width="2.6">
            <circle cx="34" cy="34" r="17"/>
            <ellipse cx="34" cy="34" rx="7.5" ry="17"/>
            <line x1="17" y1="34" x2="51" y2="34"/>
            <path d="M20 25h28M20 43h28"/>
          </g>
        </svg>
        <span class="contact-text">www.vorneltech.com</span>
      </li>
      <li class="contact-item contact-item--address">
        <svg class="contact-icon" viewBox="0 0 68 68" aria-hidden="true">
          <circle cx="34" cy="34" r="34" fill="var(--accent)"/>
          <path d="M34 52C27 43 22 36 22 29a12 12 0 0 1 24 0c0 7-5 14-12 23z" fill="#fff"/>
          <circle cx="34" cy="29" r="4.5" fill="var(--accent)"/>
        </svg>
        <span class="contact-text contact-text--address">Unit 5 Harlow Court North<br>Kingsmere Vale<br>Bristol, BS9 4QT</span>
      </li>
    </ul>
  </main>
</body>
</html>
```